Storm Restoration Contractor needs a professional letterhead design

Looking for a professional letterhead design. Not looking for your cheapo MS Word standard ones that are readily available. Dont want it to be cookie cutter look like ones readily available online. We just recently changed our logo and want to freshen up all our documents. Our company handles restoring a property back to a pre-loss condition after a storm damages it. For example, wind, hail, flood, fire losses.

Target Market(s)

Property Owners, Homeowners, Property Owners, Commercial Property Owners, Property Management Companies

Industry/Entity Type

Construction Company

Requirements
Must have
• Professional, Use 1 of 2 logo options
• Storm Restoration, Roofing, Siding, Windows

```html
<!DOCTYPE html>
<html lang="en">
<head>
<meta charset="utf-8">
<title>Northgate Exteriors — Letterhead</title>
<link rel="stylesheet" href="https://fonts.googleapis.com/css2?family=Jost:wght@400;500&display=swap">
<style>
  :root {
    --backdrop: #e9e9ea;
    --paper: #ffffff;
    --brand-blue: #1f72c4;
    --ink: #2b2b2b;
    --ink-soft: #555a61;
    --watermark: #eef1f8;
  }
  html, body {
    margin: 0;
    width: 1200px;
    height: 795px;
    overflow: hidden;
    background: var(--backdrop);
    font-family: "Jost", "Helvetica Neue", Arial, sans-serif;
  }
  .letterhead {
    position: absolute;
    left: 338px;
    top: 27px;
    width: 524px;
    height: 740px;
    background: var(--paper);
    box-shadow: 0 6px 22px rgba(0,0,0,0.12);
    overflow: hidden;
  }
  .brand {
    position: absolute;
    left: 40px;
    top: 38px;
    display: flex;
    align-items: center;
    gap: 8px;
  }
  .brand-dot {
    width: 26px;
    height: 26px;
    border-radius: 50%;
    background: var(--brand-blue);
  }
  .brand-name {
    font-weight: 500;
    font-size: 13px;
    letter-spacing: 1.5px;
    text-transform: uppercase;
    color: var(--brand-blue);
  }
  .watermark-ring {
    position: absolute;
    left: 112px;
    top: 175px;
    width: 300px;
    height: 300px;
  }
  .band {
    position: absolute;
    left: 0;
    right: 0;
    background: var(--brand-blue);
  }
  .band-upper { top: 596px; height: 7px; }
  .band-lower { top: 700px; height: 10px; }
  .contact {
    position: absolute;
    right: 26px;
    top: 612px;
    text-align: right;
    font-size: 10.5px;
    line-height: 19px;
    color: var(--ink);
  }
  .contact-name { color: var(--brand-blue); }
  .contact-lines { display: flex; justify-content: flex-end; align-items: center; gap: 4px; color: var(--brand-blue); }
  .contact-lines svg { width: 10px; height: 10px; fill: var(--ink-soft); }
  .contact-web { color: var(--brand-blue); }
</style>
</head>
<body>
  <main class="letterhead">
    <header class="brand">
      <span class="brand-dot"></span>
      <span class="brand-name">Northgate Exteriors</span>
    </header>

    <svg class="watermark-ring" viewBox="0 0 300 300" aria-hidden="true">
      <circle cx="150" cy="150" r="138" fill="none" stroke="var(--watermark)" stroke-width="22"/>
    </svg>

    <div class="band band-upper"></div>

    <footer class="contact">
      <div class="contact-name">Northgate Exteriors</div>
      <div class="contact-address">2250 Harbor Lane, Fairview, CA 95120</div>
      <div class="contact-lines">
        <svg viewBox="0 0 10 10" aria-label="Phone"><path d="M2 0.5 L3.6 2.6 L2.7 3.6 Q3.8 5.8 6.4 7.3 L7.4 6.4 L9.5 8 L8.3 9.5 Q3.5 8.8 0.5 1.7 Z"/></svg>
        <span>(555) 204-7731</span>
        <svg viewBox="0 0 10 10" aria-label="Fax"><rect x="2" y="0.5" width="6" height="3"/><rect x="0.5" y="4" width="9" height="5" rx="1"/></svg>
        <span>(555) 204-7731</span>
        <svg viewBox="0 0 10 10" aria-label="Email"><path d="M0.5 2 H9.5 V8.5 H0.5 Z M1.2 2.6 L5 5.6 L8.8 2.6" stroke="#fff" stroke-width="0.7"/></svg>
        <span>info@northgateexteriors.com</span>
      </div>
      <div class="contact-web">www.northgateexteriors.com</div>
    </footer>

    <div class="band band-lower"></div>
  </main>
</body>
</html>
```